First North America Product Category Rule

8 x 10 foot booth design for a stretch fabric wrap-around. The booth will be used in a very small exhibit area for 150 attendees. It is for the packaging industry focused on the environment. This booth graphic is NOT about our company, but to promote participation in a project we are sponsoring. The project is to develop the first North American Packaging Category Rule, so the booth is to invite conference attendees to join our effort. Production specifications are attached.

Target Market(s)

Meridian 300, Sustainability Directors, Packaging Engineers

Industry/Entity Type

Packaging; Environment

Font styles to use
Sans Serif

Requirements
Must have
• An Eye-Catching or Intriguing Image/Graphics/Letter Treatment
Should not have
• Nothing too bright or garish. All text should be above waist height (No text below the 36-40" mark)

```html
<!DOCTYPE html>
<html lang="en">
<head>
<meta charset="utf-8">
<title>First North American Product Category Rule for Protective Packaging</title>
<link rel="stylesheet" href="https://fonts.googleapis.com/css2?family=Barlow+Semi+Condensed:ital,wght@0,400;0,600;0,700;0,800;1,600&display=swap">
<style>
  :root {
    --olive: #a3a812;
    --brown: #5b2a1a;
    --teal: #3a9fbd;
    --navy: #2c4f80;
    --gold: #b8900f;
    --charcoal: #2b2b2b;
    --white: #ffffff;
    --page: #ffffff;
  }
  * { margin: 0; padding: 0; box-sizing: border-box; }
  html, body {
    width: 845px; height: 1200px; overflow: hidden;
    background: var(--page);
    font-family: "Barlow Semi Condensed", Arial, sans-serif;
  }
  .banner {
    position: absolute; left: 20px; top: 372px;
    width: 805px; height: 455px;
    background: linear-gradient(120deg, #e9e9e9 0%, #f7f7f7 35%, #efefef 60%, #f6f6f6 100%);
    box-shadow: -6px 6px 10px rgba(0,0,0,0.35);
    overflow: hidden;
  }
  .banner__top-band { position: absolute; left: 0; top: 0; width: 100%; height: 22px; background: var(--olive); }
  .banner__base-band { position: absolute; left: 0; top: 393px; width: 100%; height: 62px; background: var(--gold); }
  .shapes { position: absolute; left: 0; top: 0; }
  .kicker {
    position: absolute; left: 270px; top: 24px; width: 266px; height: 22px;
    color: var(--white); font-weight: 700; font-size: 14px; letter-spacing: 3.2px;
    text-align: center; line-height: 22px;
  }
  .title-line {
    position: absolute; left: 0; width: 100%; text-align: center;
    font-weight: 800; line-height: 1; white-space: nowrap;
  }
  .title-line--top { top: 52px; font-size: 38px; color: var(--brown); }
  .title-line--main { top: 90px; font-size: 39px; color: var(--white); }
  .subtitle {
    position: absolute; left: 260px; top: 143px; width: 413px; height: 28px;
    text-align: center; color: var(--white); font-weight: 700; font-size: 24px; line-height: 28px;
  }
  .photo {
    position: absolute; left: 265px; top: 179px; width: 445px; height: 214px;
    background:
      radial-gradient(ellipse at 55% 45%, rgba(240,215,170,0.85) 0%, rgba(240,215,170,0) 45%),
      linear-gradient(90deg, #3f5a8a 0%, #8a5a3a 35%, #c9a070 60%, #b5562e 85%, #6a3a22 100%);
  }
  .quote {
    position: absolute; left: 500px; top: 321px; width: 166px; height: 66px;
    background: rgba(25,25,25,0.85); border-radius: 6px;
    padding: 14px 8px 0 20px;
    color: var(--white); font-style: italic; font-weight: 600; font-size: 7px; line-height: 10px;
    white-space: nowrap;
  }
  .quote__mark {
    position: absolute; color: var(--white); font-style: normal; font-weight: 800; font-size: 20px; line-height: 1;
  }
  .quote__mark--open { left: 8px; top: -2px; }
  .quote__mark--close { right: 6px; bottom: -10px; }
  .step-label {
    position: absolute; width: 90px; text-align: center;
    color: var(--white); font-weight: 700; font-size: 12.5px; line-height: 13px;
    transform: translate(-50%, -50%);
  }
  .step-label--wide { font-size: 13px; line-height: 16px; }
  .step-number {
    position: absolute; color: var(--white); font-weight: 600; font-size: 18px; line-height: 1;
  }
  .credits {
    position: absolute; top: 405px; color: var(--white); font-size: 10px; font-weight: 400; white-space: nowrap;
  }
  .credits strong { font-weight: 700; }
</style>
</head>
<body>
  <section class="banner">
    <div class="banner__top-band"></div>
    <div class="photo" role="img" aria-label="Photo of a smiling warehouse worker in a blue hard hat and safety vest lifting a cardboard box onto a shelf"></div>
    <div class="banner__base-band"></div>

    <svg class="shapes" viewBox="0 0 805 455" width="805" height="455">
      <defs>
        <linearGradient id="fill-olive" x1="0" x2="1"><stop offset="0" stop-color="#9ca515"/><stop offset="1" stop-color="#7a860c"/></linearGradient>
        <linearGradient id="fill-brown" x1="0" x2="1"><stop offset="0" stop-color="#6b3222"/><stop offset="1" stop-color="#4a1f12"/></linearGradient>
        <linearGradient id="fill-gold" x1="0" x2="1"><stop offset="0" stop-color="#c1940f"/><stop offset="1" stop-color="#9c7608"/></linearGradient>
        <linearGradient id="fill-steel" x1="0" x2="1"><stop offset="0" stop-color="#6596b4"/><stop offset="1" stop-color="#4d7a98"/></linearGradient>
      </defs>
      <!-- kicker tab -->
      <polygon points="264,22 542,22 528,47 280,47" fill="var(--gold)"/>
      <polygon points="270,22 536,22 522,45 286,45" fill="var(--olive)"/>
      <!-- headline bands -->
      <polygon points="175,89 618,89 629,128 190,128" fill="var(--teal)"/>
      <polygon points="260,143 663,143 673,171 270,171" fill="var(--navy)"/>
      <!-- step 01 -->
      <circle cx="203" cy="194" r="55" fill="var(--charcoal)"/>
      <path d="M258 194 L258 280 C250 264 236 256 196 249 Z" fill="var(--charcoal)"/>
      <circle cx="203" cy="194" r="47" fill="url(#fill-olive)"/>
      <!-- step 04 -->
      <circle cx="203" cy="311" r="55" fill="var(--charcoal)"/>
      <path d="M258 311 L258 396 C250 380 236 373 196 366 Z" fill="var(--charcoal)"/>
      <circle cx="203" cy="311" r="47" fill="url(#fill-brown)"/>
      <!-- step 02 -->
      <circle cx="320" cy="234" r="55" fill="var(--charcoal)"/>
      <path d="M265 234 L265 318 C273 303 288 296 327 289 Z" fill="var(--charcoal)"/>
      <circle cx="320" cy="234" r="47" fill="url(#fill-gold)"/>
      <!-- step 03 -->
      <circle cx="320" cy="349" r="55" fill="var(--charcoal)"/>
      <path d="M265 349 L265 436 C273 420 288 412 327 404 Z" fill="var(--charcoal)"/>
      <circle cx="320" cy="349" r="47" fill="url(#fill-steel)"/>
    </svg>

    <div class="kicker">FIRST NORTH AMERICAN</div>
    <h1 class="title-line title-line--top">PRODUCT CATEGORY RULE FOR</h1>
    <h2 class="title-line title-line--main">PROTECTIVE PACKAGING</h2>
    <p class="subtitle">Enlisting Stakeholder Participation</p>

    <div class="quote">
      <span class="quote__mark quote__mark--open">&ldquo;</span>
      <p>How EPD Can Move the Dialogue<br>Beyond End-of-Life Disposal to Include<br>Environmental Benchmarks for<br>Product Production &amp; Distribution</p>
      <span class="quote__mark quote__mark--close">&rdquo;</span>
    </div>

    <p class="step-label" style="left:203px; top:194px;">PCR<br>Product<br>Category<br>Rules</p>
    <span class="step-number" style="left:234px; top:235px;">01</span>
    <p class="step-label" style="left:320px; top:234px;">LCA<br>Life Cycle<br>Assessment</p>
    <span class="step-number" style="left:270px; top:273px;">02</span>
    <p class="step-label step-label--wide" style="left:320px; top:349px;">Third Party<br>Verification</p>
    <span class="step-number" style="left:270px; top:392px;">03</span>
    <p class="step-label" style="left:203px; top:311px;">EDP<br>Registration<br>and<br>Publication</p>
    <span class="step-number" style="left:232px; top:352px;">04</span>

    <p class="credits" style="left:335px;">Sponsored by: <strong>Foam Packaging Council</strong></p>
    <p class="credits" style="left:509px;">Managed by: <strong>Open Ledger Group</strong></p>
  </section>
</body>
</html>
```